Harbor Deed needs a new brochure design

The brochure will be used as a marketing tool for Realtors, Lenders and Family Law Attorney's. I have attached the "OLD" brochure to give you an idea of our business and what we do. We want a fresh more modern design. I also attached the Logo. Please let me know if you need any further information

Target Market(s)

Realtors, mortgage professionals (home lenders), Family Law Attorneys

```html
<!DOCTYPE html>
<html lang="en">
<head>
<meta charset="utf-8">
<title>Harbor Deed Brochure</title>
<link rel="stylesheet" href="https://fonts.googleapis.com/css2?family=Raleway:wght@300;400;700&family=Roboto:wght@300;400;700&display=swap">
<style>
:root{
  --navy:#1b2f86;
  --blue-deep:#1c5494;
  --blue-soft:#4f7cb0;
  --ink:#1d1f22;
  --text:#2b2b2b;
  --line:#d6d6d6;
  --paper:#ffffff;
}
*{margin:0;padding:0;box-sizing:border-box}
html,body{width:1200px;height:1200px;overflow:hidden;background:var(--paper)}
.canvas{position:relative;width:1200px;height:1200px;background:var(--paper)}
.spread-art{position:absolute;inset:0;width:1200px;height:1200px}
.brand{position:absolute;display:flex;align-items:center;gap:8px;transform:translateX(-50%);
  font-family:"Raleway",sans-serif;font-weight:700;font-size:21px;letter-spacing:2px;color:var(--navy);white-space:nowrap}
.brand-mark{width:16px;height:16px;background:var(--navy)}
.brand--left{left:490px;top:268px}
.brand--right{left:713px;top:262px}
.about{position:absolute;left:14px;top:688px;width:445px;font-family:"Roboto",sans-serif}
.section-title{font-family:"Raleway",sans-serif;font-weight:400;font-size:26px;color:var(--navy);margin-bottom:10px}
.about p{font-size:8.6px;line-height:16.1px;color:var(--text);font-weight:300}
.connect{position:absolute;left:14px;top:851px;font-family:"Roboto",sans-serif}
.connect .section-title{margin-bottom:6px}
.connect li{list-style:none;font-size:10.5px;line-height:18.4px;color:var(--text);font-weight:300}
.tagline{position:absolute;right:18px;top:786px;text-align:right;font-family:"Raleway",sans-serif}
.tagline .light{display:block;font-weight:400;font-size:25px;line-height:30px;color:var(--paper)}
.tagline .bold{display:block;font-family:"Roboto",sans-serif;font-weight:700;font-size:24px;line-height:31px;color:var(--ink)}
.tagline .legal{display:block;font-family:"Roboto",sans-serif;font-size:15px;line-height:24px;color:var(--paper);margin-top:2px}
.web{position:absolute;left:620px;top:993px;font-family:"Roboto",sans-serif;font-size:13px;color:var(--ink)}
</style>
</head>
<body>
<div class="canvas">
  <svg class="spread-art" viewBox="0 0 1500 1500" xmlns="http://www.w3.org/2000/svg">
    <defs>
      <linearGradient id="photoWarm" x1="0" y1="0" x2="1" y2="1">
        <stop offset="0" stop-color="#c9424e"/>
        <stop offset="0.4" stop-color="#e8dcd2"/>
        <stop offset="1" stop-color="#f1f1f1"/>
      </linearGradient>
      <linearGradient id="photoCool" x1="0" y1="0" x2="1" y2="1">
        <stop offset="0" stop-color="#dfe9f2"/>
        <stop offset="0.5" stop-color="#c7cfd6"/>
        <stop offset="1" stop-color="#7f8c99"/>
      </linearGradient>
      <filter id="sheetShadow" x="-5%" y="-5%" width="110%" height="115%">
        <feDropShadow dx="0" dy="10" stdDeviation="10" flood-color="#000" flood-opacity="0.25"/>
      </filter>
    </defs>
    <rect class="sheet" x="0" y="220" width="1500" height="1060" fill="#fff" filter="url(#sheetShadow)"/>
    <polygon class="photo-handshake" role="img" aria-label="Agent in red cardigan shaking hands over a small model house"
      points="0,220 160,220 750,575 750,585 365,800 0,620" fill="url(#photoWarm)"/>
    <polyline points="160,222 525,432 525,448" fill="none" stroke="var(--line)" stroke-width="4"/>
    <polyline points="0,625 522,880 522,893" fill="none" stroke="var(--line)" stroke-width="4"/>
    <polygon class="band-left" points="365,800 750,585 750,990" fill="var(--blue-deep)"/>
    <polygon class="corner-dark" points="590,1280 750,1128 750,1280" fill="var(--ink)"/>
    <polygon class="corner-blue" points="586,1280 750,1100 750,1128 594,1280" fill="var(--blue-deep)"/>
    <polygon class="photo-meeting" role="img" aria-label="Smiling client shaking hands with an advisor in an office"
      points="750,575 1230,220 1500,220 1500,590 1185,775 1500,962 1500,1280 750,1280" fill="url(#photoCool)"/>
    <polyline points="1290,222 1075,355 1100,368" fill="none" stroke="var(--line)" stroke-width="4"/>
    <polygon points="1185,775 1500,590 1500,962" fill="#fff"/>
    <polyline points="1500,590 1188,775 1500,962" fill="none" stroke="var(--line)" stroke-width="4"/>
    <polygon class="overlay" points="750,575 1140,790 750,1025" fill="var(--blue-soft)" fill-opacity="0.7"/>
    <polygon class="band-right" points="750,1025 1140,790 1185,775 1500,962 1500,1280 1320,1280" fill="var(--blue-soft)"/>
    <polygon points="750,1025 1320,1280 750,1280" fill="#fff"/>
  </svg>

  <div class="brand brand--left"><span class="brand-mark"></span>HARBOR DEED</div>
  <div class="brand brand--right"><span class="brand-mark"></span>HARBOR DEED</div>

  <section class="about">
    <h2 class="section-title">About Us</h2>
    <p>At Harbor Deed, we have the experience and skill to effectively handle simple and complex residential real estate closings throughout Florida. We regularly work with realtors, buyers, sellers, lenders and mortgage brokers in real estate transactions ranging from single family homes to condominiums and townhomes. The closing is the most important part of the process, and the culmination of everyone's hard work. As such we dedicate ourselves to meticulous title and escrow work, as well as regular and detailed customer updates. We understand the parties each have conflicting schedules, as well as different demands on their time and will provide the flexibility needed to accommodate everyone.</p>
  </section>

  <section class="connect">
    <h2 class="section-title">Connect Us</h2>
    <ul>
      <li>mara@harbordeedFL.com</li>
      <li>harbordeedFL.com</li>
      <li>512 W, Cypress Ave</li>
      <li>Suite 310</li>
      <li>Tampa, FL 33602</li>
      <li>813-555-0192</li>
    </ul>
  </section>

  <div class="tagline">
    <span class="light">We take the Aggravation</span>
    <span class="light">and Anxiety out of</span>
    <span class="bold">BUYING,SELLING&nbsp;</span>
    <span class="bold">AND REFINANCING PROPERTY</span>
    <span class="legal">A Florida Limited Liability Company</span>
  </div>

  <div class="web">www.HarborDeedFL.com</div>
</div>
</body>
</html>
```